COVID-19 Accredited CME Impact Infographic

We want an infographic showing how much COVID-19 Continuing Medical Education we have accredited and its impact. Our website is at https://med.halvering.edu/cme/COVID19/education.html The attached document is intended to simply show the elements. You have complete freedom on design. We will be updating the numbers weekly so it is important that we have the files so that we can update it. This can be done in powerpoint, publisher, word, in-design, illustrator. Don't use crazy fonts that we wont have.

Target Market(s)

Internal to Halvering. We just want to show the impact of our work

Industry/Entity Type

Education

Requirements
Must have
• We must be able to update the numbers ourselves.

See attached document for the pieces that we want.

The sizes of the numbers in the attached are based on importance to us.
Nice to have
• Not mandatory but try to use these colors. https://med.halvering.edu/identity/color-palette.html

I was thinking that perhaps the big number could be done in traditional train. Like this: https://www.pictovane.com/image-illustration/flip-board-under-constuction-page-isolated-8803617452

```html
<!DOCTYPE html>
<html lang="en">
<head>
<meta charset="utf-8">
<title>COVID-19 CME Impact — Halvering Medicine</title>
<link rel="stylesheet" href="https://fonts.googleapis.com/css2?family=Anton&family=Questrial&display=swap">
<style>
  :root {
    --paper: #f1f1f1;
    --slate: #4a6563;
    --navy: #003057;
    --navy-ink: #0b2f57;
    --tile-light: #a8d5d2;
    --tile-edge: #2f3535;
    --tile-dark-top: #003a6e;
    --tile-dark-top-hi: #005093;
    --tile-dark-bottom: #033562;
    --glow: #7fe0e6;
    --white: #ffffff;
  }
  * { box-sizing: border-box; margin: 0; padding: 0; }
  html, body { width: 1200px; height: 1131px; overflow: hidden; background: #ffffff; }
  .canvas {
    position: relative;
    width: 1200px; height: 1095px;
    background: var(--paper);
    font-family: "Questrial", "Century Gothic", sans-serif;
  }
  .headline {
    position: absolute; left: 95px; top: 134px;
    font-family: "Anton", "Impact", sans-serif;
    font-weight: 400;
    font-size: 92px; line-height: 1; letter-spacing: 1px;
    color: var(--slate);
    transform: scaleX(1.25);
    transform-origin: left top;
    white-space: nowrap;
  }
  .headline .accent { color: var(--navy); }
  .brand {
    position: absolute; right: 82px; top: 160px;
    font-family: "Questrial", "Century Gothic", sans-serif;
    font-size: 34px; line-height: 40px;
    color: var(--navy);
    white-space: nowrap;
  }

  .label {
    position: absolute; height: 31px;
    background: var(--slate); color: var(--white);
    border-radius: 6px;
    font-size: 20.5px; line-height: 33px;
    padding-left: 22px; text-transform: uppercase;
    white-space: nowrap;
  }
  .board { position: absolute; display: flex; gap: 15px; }
  .tile {
    position: relative; width: 95px; height: 160px;
    filter: drop-shadow(22px 26px 18px rgba(120,170,175,0.28));
  }
  .tile .half {
    position: absolute; left: 0; width: 95px; height: 77px;
    border-radius: 6px;
  }
  .tile .top { top: 0; }
  .tile .bottom { bottom: 0; }
  .tile.light .half { background: var(--tile-light); border: 2px solid var(--tile-edge); }
  .tile.dark .top {
    background: linear-gradient(135deg, var(--tile-dark-top) 30%, var(--tile-dark-top-hi));
    box-shadow: 0 0 4px var(--glow);
  }
  .tile.dark .bottom {
    background: var(--tile-dark-bottom);
    border: 2px solid #0a1e33;
    box-shadow: 0 -1px 4px var(--glow);
  }
  .tile .digit {
    position: absolute; inset: 0;
    display: flex; align-items: center; justify-content: center;
    font-size: 134px; line-height: 1; padding-top: 4px;
  }
  .tile.light .digit { color: var(--navy-ink); }
  .tile.dark .digit { color: var(--white); }
</style>
</head>
<body>
<main class="canvas">
  <h1 class="headline">COVID-19<span class="accent">CME</span></h1>
  <div class="brand">Halvering Medicine</div>

  <!-- States -->
  <div class="label" style="left:92px;top:267px;width:173px;">Of States</div>
  <div class="board" style="left:93px;top:313px;">
    <div class="tile light"><div class="half top"></div><div class="half bottom"></div><span class="digit">2</span></div>
    <div class="tile light"><div class="half top"></div><div class="half bottom"></div><span class="digit">6</span></div>
  </div>

  <!-- Countries -->
  <div class="label" style="left:344px;top:267px;width:173px;">Of Countries</div>
  <div class="board" style="left:345px;top:313px;">
    <div class="tile light"><div class="half top"></div><div class="half bottom"></div><span class="digit">1</span></div>
    <div class="tile light"><div class="half top"></div><div class="half bottom"></div><span class="digit">2</span></div>
  </div>

  <!-- Activities -->
  <div class="label" style="left:673px;top:267px;width:173px;">Of Activities</div>
  <div class="board" style="left:673px;top:313px;gap:16px;">
    <div class="tile dark"><div class="half top"></div><div class="half bottom"></div><span class="digit">2</span></div>
    <div class="tile dark"><div class="half top"></div><div class="half bottom"></div><span class="digit">3</span></div>
  </div>
  <div class="board" style="left:914px;top:313px;gap:16px;">
    <div class="tile light"><div class="half top"></div><div class="half bottom"></div></div>
    <div class="tile light"><div class="half top"></div><div class="half bottom"></div></div>
  </div>

  <!-- CME learners -->
  <div class="label" style="left:92px;top:533px;width:205px;">Of CME Learners</div>
  <div class="board" style="left:93px;top:583px;">
    <div class="tile light"><div class="half top"></div><div class="half bottom"></div><span class="digit">5</span></div>
    <div class="tile light"><div class="half top"></div><div class="half bottom"></div><span class="digit">8</span></div>
  </div>
  <div class="board" style="left:345px;top:583px;">
    <div class="tile light"><div class="half top"></div><div class="half bottom"></div><span class="digit">7</span></div>
    <div class="tile light"><div class="half top"></div><div class="half bottom"></div><span class="digit">9</span></div>
  </div>

  <!-- Live learners -->
  <div class="label" style="left:673px;top:533px;width:205px;">Of Live Learners</div>
  <div class="board" style="left:673px;top:583px;gap:16px;">
    <div class="tile dark"><div class="half top"></div><div class="half bottom"></div><span class="digit">2</span></div>
    <div class="tile dark"><div class="half top"></div><div class="half bottom"></div><span class="digit">3</span></div>
  </div>
  <div class="board" style="left:914px;top:583px;gap:16px;">
    <div class="tile light"><div class="half top"></div><div class="half bottom"></div><span class="digit">1</span></div>
    <div class="tile light"><div class="half top"></div><div class="half bottom"></div><span class="digit">2</span></div>
  </div>

  <!-- On-demand views -->
  <div class="label" style="left:92px;top:789px;width:364px;">Of Total On-Demand Views</div>
  <div class="board" style="left:93px;top:837px;gap:16px;">
    <div class="tile dark"><div class="half top"></div><div class="half bottom"></div><span class="digit">1</span></div>
    <div class="tile dark"><div class="half top"></div><div class="half bottom"></div><span class="digit">2</span></div>
  </div>
  <div class="board" style="left:344px;top:837px;gap:19px;">
    <div class="tile dark"><div class="half top"></div><div class="half bottom"></div><span class="digit">0</span></div>
    <div class="tile dark"><div class="half top"></div><div class="half bottom"></div><span class="digit">9</span></div>
    <div class="tile dark"><div class="half top"></div><div class="half bottom"></div><span class="digit">9</span></div>
    <div class="tile dark"><div class="half top"></div><div class="half bottom"></div><span class="digit">8</span></div>
    <div class="tile dark"><div class="half top"></div><div class="half bottom"></div><span class="digit">7</span></div>
    <div class="tile dark"><div class="half top"></div><div class="half bottom"></div></div>
    <div class="tile dark"><div class="half top"></div><div class="half bottom"></div></div>
  </div>
</main>
</body>
</html>
```